Course Lantern

CourseLantern.example will be a place for people looking for information, resources, and advisement to start or continue their education. We want a friendly, inviting site design that makes finding what potential students are looking for simple and easy to navigate. We are not committed to the colors of the logo, so variations on the color scheme are welcome.

Text instructions based on the wireframe: For the site's homepage we'd like a banner at the very top for our Logo and white space to the right of it. See attachments for logo + wireframe. Below that would be navigation. Below that split into 2/3 on the left we would have home page content, and 1/3 on the right we would have the lead form. At the bottom of the page we would have a space for types of degrees, then a footer with copyright info + site info.

See wireframes for additional page layouts.

Industry/Entity Type

Education

Requirements
Must have
• At minimum we are looking for three pages: homepage, choose your degree path page, and content page.
Nice to have
• -White space is appreciated
-Variations on the color scheme are welcome, we are not married to the existing logo's color scheme.

```html
<!DOCTYPE html>
<html lang="en">
<head>
<meta charset="utf-8">
<title>Course Lantern</title>
<link rel="stylesheet" href="https://fonts.googleapis.com/css2?family=Ubuntu:ital,wght@0,400;0,500;1,400;1,500&display=swap">
<style>
:root{
  --dark:#3b3b3b;
  --dark-2:#333333;
  --orange:#f25a0f;
  --orange-deep:#e63a06;
  --title:#e2360f;
  --label:#f06a14;
  --text:#333333;
  --rule:#dddddd;
  --frame:#dcdcdc;
  --field-border:#cfcfcf;
  --placeholder:#a9a9a9;
  --sky-top:#c6e6f7;
}
*{box-sizing:border-box;margin:0;padding:0}
html,body{width:1094px;height:1200px;overflow:hidden}
body{position:relative;background:#fff;font-family:"Ubuntu",sans-serif;color:var(--text)}

.site-header{position:absolute;left:0;top:0;width:1094px;height:140px;background:var(--dark)}
.brand{position:absolute;left:118px;top:66px;display:flex;align-items:center;gap:12px}
.brand-mark{width:22px;height:22px;background:var(--orange)}
.brand-name{font-size:40px;font-weight:500;color:#fff;letter-spacing:-0.5px;line-height:1}
.contact{position:absolute;right:114px;top:18px;text-align:right;line-height:23px}
.contact-label{color:var(--orange);font-size:12px;font-weight:500}
.contact-value{color:#fff;font-size:17px;margin-left:4px}
.contact-email{font-style:italic;text-decoration:underline}
.main-nav{position:absolute;left:473px;top:81px;width:507px;height:42px;border-radius:10px;
  background:linear-gradient(#f7731c,#e8480a);display:flex;overflow:hidden}
.main-nav a{flex:1;display:flex;align-items:center;justify-content:center;color:#fff;
  font-size:12px;text-decoration:none;border-left:1px solid #f38a4f}
.main-nav a:first-child{border-left:0;background:linear-gradient(#f25e12,#dc3b05)}

.hero{position:absolute;left:0;top:140px;width:1094px;height:407px;
  background:linear-gradient(var(--sky-top),#ffffff)}
.hero svg{display:block}

.card{position:absolute;top:569px;height:547px;border:7px solid var(--frame);border-radius:12px;background:#fff}
.card-welcome{left:109px;width:496px}
.card-lead{left:619px;width:367px}
.card h2,.card h3{position:absolute;font-style:italic;font-weight:500;color:var(--title);
  border-bottom:1px solid var(--rule)}
.card h2{font-size:20px;height:32px}
.card h3{font-size:16px;height:22px}
.copy{position:absolute;font-size:11px;line-height:13.2px}
.copy p+p{margin-top:13px}
.read-more{position:absolute;font-size:11px;font-style:italic;color:var(--title);text-decoration:underline}
.thumb{position:absolute;width:153px;height:96px}

.intro{position:absolute;left:20px;top:60px;width:300px;font-size:11px;font-style:italic;line-height:13.5px}
.intro p+p{margin-top:13px}
.lead-form{position:absolute;left:20px;top:129px;width:310px}
.field{height:41px}
.field label{display:block;font-size:10px;color:var(--label);height:12px;line-height:12px}
.input{height:18px;border:1px solid var(--field-border);font-size:10px;font-style:italic;color:var(--placeholder);
  padding-left:8px;line-height:16px;position:relative;background:#fff}
.select::after{content:"";position:absolute;right:-1px;top:-1px;width:18px;height:18px;background:var(--orange)}
.select::before{content:"";position:absolute;right:5px;top:6px;z-index:1;border:4px solid transparent;border-top:5px solid #fff}
.row{display:flex;gap:5px}
.submit{display:block;width:134px;height:29px;background:var(--orange);border:0;color:#fff;
  font-family:"Ubuntu",sans-serif;font-size:13px;margin-top:-2px}
.required{position:absolute;left:21px;top:508px;font-size:11px;font-style:italic;color:var(--label)}

.site-footer{position:absolute;left:0;top:1085px;width:1094px;height:115px;background:var(--dark-2)}
.footer-links{position:absolute;top:61px;width:100%;text-align:center;color:#fff;font-size:10px;line-height:14px}
.footer-links a{color:#fff;text-decoration:none;margin:0 4px}
</style>
</head>
<body>

<header class="site-header">
  <div class="brand"><span class="brand-mark"></span><span class="brand-name">Course Lantern</span></div>
  <div class="contact">
    <div><span class="contact-label">Call:</span><span class="contact-value">111-111-111</span></div>
    <div><span class="contact-label">Email:</span><span class="contact-value contact-email">Info@courselantern.example</span></div>
  </div>
  <nav class="main-nav">
    <a href="#">About Us</a><a href="#">Contact Us</a><a href="#">Privacy Policy</a><a href="#">Terms of Use</a><a href="#">Feed Back</a>
  </nav>
</header>

<section class="hero">
  <svg width="1094" height="407" viewBox="0 0 1094 407">
    <defs>
      <linearGradient id="sky" x1="0" y1="0" x2="0" y2="1"><stop offset="0" stop-color="#6fa6dc"/><stop offset=".55" stop-color="#2b3a5c"/><stop offset="1" stop-color="#4a6a3a"/></linearGradient>
      <linearGradient id="warm" x1="0" y1="0" x2="0" y2="1"><stop offset="0" stop-color="#8e9a5a"/><stop offset=".5" stop-color="#3a2e28"/><stop offset="1" stop-color="#111"/></linearGradient>
      <linearGradient id="navy" x1="0" y1="0" x2="0" y2="1"><stop offset="0" stop-color="#2c3a55"/><stop offset=".5" stop-color="#9a7a6a"/><stop offset="1" stop-color="#0c1424"/></linearGradient>
      <linearGradient id="olive" x1="0" y1="0" x2="0" y2="1"><stop offset="0" stop-color="#4e5a3a"/><stop offset=".5" stop-color="#c29a7a"/><stop offset="1" stop-color="#1a1a14"/></linearGradient>
      <linearGradient id="blue" x1="0" y1="0" x2="0" y2="1"><stop offset="0" stop-color="#2a4fa0"/><stop offset="1" stop-color="#1a2f6a"/></linearGradient>
    </defs>
    <polygon role="img" aria-label="Graduates throwing caps into a blue sky" points="109,102 283,76 283,384 109,357" fill="url(#sky)"/>
    <rect role="img" aria-label="Two smiling graduates holding diplomas" x="283" y="11" width="174" height="307" fill="url(#warm)"/>
    <rect role="img" aria-label="Handshake while a diploma is handed over" x="457" y="48" width="174" height="306" fill="url(#navy)"/>
    <rect role="img" aria-label="Graduate adjusting her cap" x="631" y="75" width="175" height="307" fill="url(#olive)"/>
    <polygon role="img" aria-label="Hand raising a rolled diploma against a blue sky" points="806,11 980,39 980,290 806,316" fill="url(#blue)"/>
  </svg>
</section>

<footer class="site-footer">
  <div class="footer-links">
    <div><a href="#">About us</a>|<a href="#">Contact Us</a>|<a href="#">Privacy Policy</a>|<a href="#">Terms of Use</a>|<a href="#">Feed back</a></div>
    <div>Copyright © 2012. Course Lantern. All Rights Reserved</div>
  </div>
</footer>

<main>
  <article class="card card-welcome">
    <h2 style="left:15px;top:13px;width:451px">Welcome to Course Lantern</h2>
    <div class="copy" style="left:15px;top:53px;width:451px;text-align:justify">
      <p>The Neighbourhoods Forward Programme is a long term plan for improving the living conditions and prospects for people in the most disadvantaged communities in Wales. The programme ensures that the money and support available from the Regional Assembly Government and various other publicly funded agencies are targeted at the poorest areas Our role is to coordinate community led regeneration of the area with local residents, through Riverside Valley Partnership Board, seeking cooperation from other organisations within the public, private and voluntary sector to work together with us to tackle many issues that affect the lives of people who live in the area.</p>
    </div>
    <a class="read-more" href="#" style="left:15px;top:178px">Read More</a>

    <h3 style="left:15px;top:206px;width:451px">Degree Type 1</h3>
    <div class="thumb" role="img" aria-label="Group of cheerful graduates in caps" style="left:15px;top:240px;background:linear-gradient(#6a5a50,#1c1c20)"></div>
    <div class="copy" style="left:184px;top:241px;width:282px">
      <p>Are you overwhelmed by the thought of choosing the right college?</p>
      <p>CourseLantern helps simplify this process by matching colleges to you and your needs.Tell us about yourself and let us do the work for you.Are you overwhelmed by the thought.</p>
    </div>
    <a class="read-more" href="#" style="left:184px;top:350px">Read More</a>

    <h3 style="left:15px;top:373px;width:451px">Degree Type 2</h3>
    <div class="thumb" role="img" aria-label="Row of graduates in gowns" style="left:15px;top:408px;background:linear-gradient(#8a9aaa,#1e1e24)"></div>
    <div class="copy" style="left:184px;top:409px;width:282px">
      <p>Are you overwhelmed by the thought of choosing the right college?</p>
      <p>CourseLantern helps simplify this process by matching colleges to you and your needs.Tell us about yourself and let us do the work for you.Are you overwhelmed by the thought.</p>
    </div>
    <a class="read-more" href="#" style="left:184px;top:518px">Read More</a>
  </article>

  <aside class="card card-lead">
    <h2 style="left:20px;top:13px;width:313px">Tell us more about YOU!</h2>
    <div class="intro">
      <p>CourseLantern provides you with accredited school information that match your interests.</p>
      <p>Get matched to the right schools today.</p>
    </div>
    <form class="lead-form">
      <div class="field"><label>Subject*</label><div class="input select">Choose One</div></div>
      <div class="field"><label>Degree Level*</label><div class="input select">Choose One</div></div>
      <div class="field"><label>High School Grad Yr.*</label><div class="input select">Choose One</div></div>
      <div class="field"><label>First Name*</label><div class="input">Enter First Name</div></div>
      <div class="field"><label>Last Name*</label><div class="input">Enter Last Name</div></div>
      <div class="field"><label>Street Address*</label><div class="input">Enter Street Address</div></div>
      <div class="field"><label>Zip / City / State*</label>
        <div class="row"><div class="input" style="width:69px"></div><div class="input" style="width:151px"></div><div class="input" style="width:80px"></div></div>
      </div>
      <div class="field"><label>Phone Number*</label><div class="input">(&nbsp;&nbsp;&nbsp;)</div></div>
      <div class="field"><label>Email Address*</label><div class="input">Email Address</div></div>
      <button class="submit" type="button">Request Information</button>
    </form>
    <div class="required">*Required fields</div>
  </aside>
</main>

</body>
</html>
```